High-end Management Consulting Website

I am looking for a design that feels very high end and professional and very serious feeling. I would like a site that uses a lot of white space, with colors in the blue, grey family. You can use a very small about of the orange and green in the logo, but it needs to be a very small amount.

I like images similar to a rock climber helping another one up a mountain. I would love other imagery throughout the site of mountain ranges and people making it to the top.

When you think of the feel imagine people in suites, very corporate feeling. Very much focused on helping company leadership and CEOs solve problems.

From a functionality standpoint https://ninefarthingmoor.com has a good deal of similar content- However, I do not like the colors or the design. I like graphics on websites similar to https://www.bramblecrestholdings.com.

I like clean with lots of white space.

The link below has all of the content and design comments. https://files.quillorbit.com/sheet/d/7KPzXa2LmQ9vTcRw4HbN8sYdE3fUoJ6gZt5VkMnB0wA/view?usp=open

Target Market(s)

High end businesses and very experienced executives.

Industry/Entity Type

Consulting

Coding

Coded - Design and coding required

Number of Pages Required

5+ page

Font styles to use
Sans Serif

Colors

Designer to choose colors to be used in the design.

Requirements
Must have
• white space, blues some gray, clean feel VERY LITTLE use of accent colors.

I want to have a centered navigation bar.
I would like to have a secondary scrolling image.
Nice to have
• High end imagery that speaks to what is being said in the site.
This is not the main image I want to see but I like imagery like this for the main home page.
https://www.pixelharborstock.com/image-photo/couple-hiking-help-each-other-silhouette-917264305
Should not have
• Please do not use dated images or blocky feeling. Please also do not go overboard using the icon in the design.

```html
<!DOCTYPE html>
<html lang="en">
<head>
<meta charset="utf-8">
<title>Summitline Partners — Management Consulting</title>
<link href="https://fonts.googleapis.com/css2?family=Lato:wght@300;400;700;900&display=swap" rel="stylesheet">
<style>
:root{
  --blue:#2f80cc;
  --blue-nav:#3b8fd9;
  --blue-deep:#1f4f7c;
  --ink:#1e2024;
  --text:#4a4d52;
  --muted:#777b80;
  --light:#f3f4f6;
  --lighter:#f8f9fa;
  --line:#d9dce0;
  --accent:#f26322;
  --white:#ffffff;
}
*{box-sizing:border-box;margin:0;padding:0}
html,body{width:1200px;height:4250px;overflow:hidden}
body{font-family:'Lato',sans-serif;color:var(--text);background:var(--white);position:relative}
.abs{position:absolute}
.btn-accent{position:absolute;background:var(--accent);color:var(--white);font-weight:700;text-transform:uppercase;display:flex;align-items:center;justify-content:center;font-size:17px}

/* header */
.header{position:absolute;left:0;top:0;width:1200px;height:115px;background:var(--white)}
.brand{position:absolute;display:flex;align-items:center;gap:12px}
.brand-mark{width:26px;height:26px;background:var(--blue)}
.brand-name{font-weight:700;color:var(--blue-deep);letter-spacing:1px;text-transform:uppercase}
.header .brand{left:110px;top:38px}
.header .brand-name{font-size:24px}
.phone{position:absolute;left:738px;top:22px;font-size:19px;color:var(--ink)}
.login{left:928px;top:15px;width:160px;height:40px;font-size:15px}
.nav{position:absolute;right:112px;top:78px;display:flex;gap:27px;font-size:17px;color:var(--ink);text-transform:uppercase}
.nav .active{color:var(--blue-nav)}

/* hero */
.hero{position:absolute;left:0;top:115px;width:1200px;height:627px}
.hero-copy{position:absolute;left:110px;top:75px;color:var(--white)}
.hero-lead{font-size:52px;font-weight:400;line-height:70px}
.hero-title{font-size:98px;font-weight:900;line-height:102px;margin-top:22px;letter-spacing:-1px}
.hero-btn{position:absolute;left:110px;top:470px;width:243px;height:66px;border:2px solid var(--white);color:var(--white);font-weight:700;font-size:19px;display:flex;align-items:center;justify-content:center}

/* intro & team */
.intro{position:absolute;left:150px;top:788px;width:900px;text-align:center;font-size:20px;line-height:41px;color:var(--text)}
.arrow{position:absolute;top:1030px;width:20px;height:30px}
.member{position:absolute;text-align:center;font-size:23px;color:var(--text)}
.member svg{display:block}
.team-note{position:absolute;left:170px;top:1236px;width:860px;text-align:center;font-size:14px;line-height:30px;color:var(--muted)}

/* experience */
.experience{position:absolute;left:0;top:1395px;width:1200px;height:723px;background:var(--light)}
.section-title{position:absolute;left:0;width:1200px;text-align:center;font-weight:900;color:var(--ink);text-transform:uppercase}
.experience .section-title{top:55px;font-size:46px}
.client{position:absolute;width:200px;text-align:center;font-size:26px;color:#3a3d42}
.view-more{left:515px;top:613px;width:170px;height:54px}

/* help */
.help .section-title{top:2178px;font-size:46px}
.service{position:absolute;width:270px;text-align:center}
.service-label{font-size:19px;line-height:30px;color:var(--ink);margin-top:26px}

/* global */
.global{position:absolute;left:0;top:2565px;width:1200px;height:810px;background:var(--lighter)}
.global-heading{position:absolute;left:200px;top:45px;width:800px;text-align:center;font-size:30px;line-height:42px;color:var(--ink);font-weight:700}
.learn{left:468px;top:210px;width:265px;height:53px;font-size:16px}

/* contact */
.contact{position:absolute;left:0;top:3375px;width:1200px;height:585px}
.contact-title{position:absolute;left:583px;top:60px;font-size:48px;font-weight:900;color:var(--white)}
.field{position:absolute;background:var(--white);color:var(--muted);font-size:15px;padding:10px 12px;border:1px solid #c9d6e4}
.agree{position:absolute;left:592px;top:408px;display:flex;align-items:center;gap:10px;color:var(--white);font-size:16px}
.agree span.box{width:14px;height:14px;border:1px solid var(--white);background:transparent}
.submit{left:590px;top:465px;width:130px;height:50px;font-size:19px}

/* footer */
.footer .brand{left:110px;top:4050px}
.footer .brand-name{font-size:25px}
.foot-head{position:absolute;top:4012px;font-size:19px;color:var(--ink);text-transform:uppercase}
.foot-list{position:absolute;top:4058px;font-size:15px;line-height:28px;color:var(--text);list-style:none}
.foot-list li{display:flex;align-items:center;gap:8px}
.rule{position:absolute;left:110px;top:4176px;width:980px;height:1px;background:var(--line)}
.copy{position:absolute;left:110px;top:4203px;font-size:14px;color:var(--muted)}
.social{position:absolute;top:4190px;width:42px;height:42px;border-radius:50%;border:1px solid var(--accent)}
</style>
</head>
<body>

<header class="header">
  <div class="brand"><span class="brand-mark"></span><span class="brand-name">Summitline Partners</span></div>
  <div class="phone">
    <svg width="14" height="14" viewBox="0 0 24 24"><path fill="#2f80cc" d="M6.6 10.8a15 15 0 0 0 6.6 6.6l2.2-2.2c.3-.3.7-.4 1-.2 1.1.4 2.3.6 3.6.6.6 0 1 .4 1 1V20c0 .6-.4 1-1 1A17 17 0 0 1 3 4c0-.6.4-1 1-1h3.5c.6 0 1 .4 1 1 0 1.3.2 2.5.6 3.6.1.3 0 .7-.2 1z"/></svg>
    1 555 0100 2200
  </div>
  <div class="btn-accent login">Expert Login</div>
  <nav class="nav">
    <span class="active">Home</span><span>Advisory Services</span><span>About</span><span>Work With Us</span>
  </nav>
</header>

<section class="hero">
  <svg class="abs" style="left:0;top:0" width="1200" height="627" viewBox="0 0 1200 627">
    <defs>
      <linearGradient id="dusk" x1="0" y1="0" x2="0" y2="1">
        <stop offset="0" stop-color="#5d7189"/>
        <stop offset=".38" stop-color="#8b8e95"/>
        <stop offset=".5" stop-color="#c98b62"/>
        <stop offset=".62" stop-color="#5c6673"/>
        <stop offset="1" stop-color="#39414c"/>
      </linearGradient>
      <linearGradient id="cliff" x1="0" y1="0" x2="1" y2="1">
        <stop offset="0" stop-color="#7fb2de"/>
        <stop offset="1" stop-color="#2f6fb3"/>
      </linearGradient>
    </defs>
    <rect role="img" aria-label="Mountain range at dusk seen from a high summit" width="870" height="627" fill="url(#dusk)"/>
    <polygon fill="#ffffff" points="820,0 870,0 785,330 870,627 820,627 738,330"/>
    <polygon role="img" aria-label="Climber resting on a rock ledge above a valley" fill="url(#cliff)" points="870,0 1200,0 1200,627 870,627 785,330"/>
  </svg>
  <div class="hero-copy">
    <div class="hero-lead">In Times of Economic<br>Uncertainty--</div>
    <div class="hero-title">YOU NEED<br>AN EDGE</div>
  </div>
  <div class="hero-btn">EXPLORE SERVICES</div>
</section>

<p class="intro">As industry leaders, former company founders, active investors and senior innovation experts, we bring experience, knowledge and connections to our engagements. Leading to cost and time savings, higher opportunity utilization and better business outcomes.</p>

<svg class="arrow" style="left:64px" viewBox="0 0 20 30"><path d="M15 4 5 15l10 11" fill="none" stroke="#888" stroke-width="2.5"/></svg>
<svg class="arrow" style="left:1115px" viewBox="0 0 20 30"><path d="M5 4l10 11-10 11" fill="none" stroke="#888" stroke-width="2.5"/></svg>

<div class="member" style="left:112px;top:962px"><svg width="170" height="170"><circle role="img" aria-label="Portrait of partner Lena" cx="85" cy="85" r="85" fill="#c9d3dd"/></svg><div style="margin-top:14px">Lena</div></div>
<div class="member" style="left:312px;top:962px"><svg width="170" height="170"><circle role="img" aria-label="Portrait of partner Cole" cx="85" cy="85" r="85" fill="#b9c3cc"/></svg><div style="margin-top:14px">Cole</div></div>
<div class="member" style="left:490px;top:942px"><svg width="216" height="216"><circle cx="108" cy="108" r="108" fill="#e6e8eb"/><circle role="img" aria-label="Portrait of partner Idris" cx="108" cy="108" r="100" fill="#8fb0cf"/></svg><div style="margin-top:12px">Idris</div></div>
<div class="member" style="left:715px;top:962px"><svg width="170" height="170"><circle role="img" aria-label="Portrait of partner Reid" cx="85" cy="85" r="85" fill="#aeb8c4"/></svg><div style="margin-top:14px">Reid</div></div>
<div class="member" style="left:915px;top:962px"><svg width="170" height="170"><circle role="img" aria-label="Portrait of partner Anton" cx="85" cy="85" r="85" fill="#c3ccd6"/></svg><div style="margin-top:14px">Anton</div></div>

<p class="team-note">Our partners have served in executive leadership for fortune 1000 global organizations, served at the highest levels of office and managed billions in buy and sell side transactions. Our experience, founding, scaling, exiting and acquiring companies along the way, gives our team a unique understanding of the clients we serve.</p>

<section class="experience">
  <h2 class="section-title">Our Experience</h2>
  <div class="client" style="left:78px;top:190px">Harlow Reeve</div>
  <div class="client" style="left:258px;top:190px">NORTHFEST</div>
  <div class="client" style="left:460px;top:190px">Ashcombe College</div>
  <div class="client" style="left:682px;top:190px">Civic Assembly</div>
  <div class="client" style="left:890px;top:190px">Veltrane</div>
  <div class="client" style="left:60px;top:345px">KVB Media</div>
  <div class="client" style="left:285px;top:345px">Orvane</div>
  <div class="client" style="left:475px;top:345px">Parcelo</div>
  <div class="client" style="left:680px;top:345px">The Marlow Group</div>
  <div class="client" style="left:905px;top:345px">Telora Capital</div>
  <div class="client" style="left:60px;top:500px">Roamly</div>
  <div class="client" style="left:295px;top:500px">Westbrook</div>
  <div class="client" style="left:475px;top:500px">Calder Group</div>
  <div class="client" style="left:690px;top:500px">Trade Office</div>
  <div class="client" style="left:900px;top:500px">CardLedger.com</div>
  <div class="btn-accent view-more">View More</div>
</section>

<section class="help">
  <h2 class="section-title">How We Help</h2>
  <div class="service" style="left:60px;top:2275px">
    <svg width="165" height="145" viewBox="0 0 165 145"><polygon points="41,1 124,1 164,72 124,144 41,144 1,72" fill="none" stroke="#9aa0a6"/><rect x="62" y="45" width="42" height="30" rx="3" fill="none" stroke="#2f80cc" stroke-width="2.5"/><path d="M62 100h42" stroke="#2f80cc" stroke-width="2.5"/></svg>
    <div class="service-label">Executive Advisory<br>Services</div>
  </div>
  <div class="service" style="left:330px;top:2275px">
    <svg width="165" height="145" viewBox="0 0 165 145"><polygon points="41,1 124,1 164,72 124,144 41,144 1,72" fill="none" stroke="#9aa0a6"/><rect x="64" y="35" width="38" height="50" fill="none" stroke="#2f80cc" stroke-width="2.5"/><path d="M71 50h24M71 60h24M71 70h24" stroke="#2f80cc" stroke-width="2"/></svg>
    <div class="service-label">Business Model Design<br>&amp; Implementation</div>
  </div>
  <div class="service" style="left:600px;top:2275px">
    <svg width="165" height="145" viewBox="0 0 165 145"><polygon points="41,1 124,1 164,72 124,144 41,144 1,72" fill="none" stroke="#9aa0a6"/><circle cx="82" cy="72" r="26" fill="none" stroke="#2f80cc" stroke-width="2.5"/><circle cx="82" cy="72" r="9" fill="none" stroke="#2f80cc" stroke-width="2.5"/></svg>
    <div class="service-label">Turnaround and<br>Restructuring</div>
  </div>
  <div class="service" style="left:870px;top:2275px">
    <svg width="165" height="145" viewBox="0 0 165 145"><polygon points="41,1 124,1 164,72 124,144 41,144 1,72" fill="none" stroke="#9aa0a6"/><path d="M60 95 80 75l12 10 18-22" fill="none" stroke="#2f80cc" stroke-width="2.5"/><path d="M100 63h10v10" fill="none" stroke="#2f80cc" stroke-width="2.5"/></svg>
    <div class="service-label">Revenue<br>Enhancement</div>
  </div>
</section>

<section class="global">
  <h2 class="global-heading">Global experience. Local market expertise. Our network of international business C-Suite executives represents every major business sector.</h2>
  <div class="btn-accent learn">Ready to Learn More?</div>
  <svg class="abs" style="left:140px;top:315px" width="920" height="420"><rect role="img" aria-label="World map drawn as a network of connected points" width="920" height="420" rx="8" fill="#eceef1"/></svg>
</section>

<section class="contact">
  <svg class="abs" style="left:0;top:0" width="1200" height="585" viewBox="0 0 1200 585">
    <defs>
      <linearGradient id="city" x1="0" y1="0" x2="0" y2="1">
        <stop offset="0" stop-color="#6f9fcf"/>
        <stop offset=".55" stop-color="#4f7394"/>
        <stop offset="1" stop-color="#2e4a5c"/>
      </linearGradient>
    </defs>
    <rect x="440" width="760" height="585" fill="#3284cf"/>
    <polygon fill="#ffffff" points="0,0 460,0 560,292 460,585 0,585"/>
    <polygon role="img" aria-label="City skyline with a bridge over a river at dusk" fill="url(#city)" points="30,0 418,0 518,292 418,585 30,585 0,292"/>
  </svg>
  <h2 class="contact-title">CONTACT US</h2>
  <div class="field" style="left:588px;top:133px;width:502px;height:38px">Name</div>
  <div class="field" style="left:588px;top:187px;width:240px;height:38px">Email</div>
  <div class="field" style="left:842px;top:187px;width:248px;height:38px">Phone</div>
  <div class="field" style="left:588px;top:241px;width:502px;height:38px">Address</div>
  <div class="field" style="left:588px;top:295px;width:502px;height:85px">Messsage</div>
  <div class="agree"><span class="box"></span>I agree to the Terms of Service and Privacy Notices</div>
  <div class="btn-accent submit">Submit</div>
</section>

<footer class="footer">
  <div class="brand"><span class="brand-mark"></span><span class="brand-name">Summitline Partners</span></div>
  <div class="foot-head" style="left:485px">Information</div>
  <ul class="foot-list" style="left:485px"><li>Home</li><li>Advisory Services</li><li>About</li><li>Work with us</li></ul>
  <div class="foot-head" style="left:743px">Contact Us</div>
  <ul class="foot-list" style="left:743px;line-height:39px">
    <li><svg width="10" height="14" viewBox="0 0 10 14"><path d="M5 0a5 5 0 0 0-5 5c0 4 5 9 5 9s5-5 5-9a5 5 0 0 0-5-5z" fill="#f26322"/></svg>Neque porro quisquam est, qui</li>
    <li><svg width="12" height="10" viewBox="0 0 12 10"><rect width="12" height="10" fill="#f26322"/><path d="M0 0l6 5 6-5" fill="none" stroke="#fff"/></svg>info@summitlinepartners.com</li>
    <li><svg width="12" height="12" viewBox="0 0 24 24"><path fill="#f26322" d="M6.6 10.8a15 15 0 0 0 6.6 6.6l2.2-2.2c.3-.3.7-.4 1-.2 1.1.4 2.3.6 3.6.6.6 0 1 .4 1 1V20c0 .6-.4 1-1 1A17 17 0 0 1 3 4c0-.6.4-1 1-1h3.5c.6 0 1 .4 1 1 0 1.3.2 2.5.6 3.6.1.3 0 .7-.2 1z"/></svg>1 555 0100 220</li>
  </ul>
  <div class="rule"></div>
  <div class="copy">© 2020 Summitline Partners. All Rights Reserved.</div>
  <span class="social" style="left:837px"></span>
  <span class="social" style="left:884px"></span>
  <span class="social" style="left:936px"></span>
  <span class="social" style="left:985px"></span>
</footer>

</body>
</html>
```